Website design for a hair building fibre

Hi I’m needing a website made for both men and women to purchase the product is a hair building fibre that you apply to thinning hair to make your hair look really thick I’ll need the website to be easy to use professional and also very classy I will need it to work with moss quill vel dor and credit cards I’ll need to have the CEO words and everything ready so I can sell I don’t have photos that I want to put on there so I’ll need a website designer to assist me in having the beautiful photos on there I know very little about websites so I need someone to be able to do it all for me

I can only provide photos of the colours of the products
I believe there will be 8 colours to sell as well
I’ve uploaded a photo of the logo I’d really like it if the website designer can check other competitors website so my website does not look like theres, I don’t want my website to look like a copied website of the competitors I’m located in Australia.
I’m also looking for someone who can open up a Wendoral and Pluvestra page and then can unload photos on them ready for consumers to view and buy.

```html
<!DOCTYPE html>
<html lang="en">
<head>
<meta charset="utf-8">
<title>Velmora Hairs — Hair Building Fibre</title>
<link href="https://fonts.googleapis.com/css2?family=Montserrat:wght@300;400;500;600;700;800&display=swap" rel="stylesheet">
<style>
:root{
  --navy:#0f1a2a;
  --sky:#7dd8f5;
  --ink:#14181f;
  --text:#6b6f76;
  --line:#d9dcdf;
  --pale:#eef8fb;
  --white:#ffffff;
  --new:#e8194a;
  --sale:#d8c21a;
  --sale-2:#2bbfa6;
  --date:#3aa9d6;
}
*{box-sizing:border-box;margin:0;padding:0}
html,body{width:1200px;height:3363px;overflow:hidden}
body{position:relative;background:var(--white);font-family:'Montserrat',sans-serif;color:var(--ink)}

/* Header */
.site-header{position:absolute;left:0;top:0;width:1200px;height:111px;background:var(--navy)}
.brand{position:absolute;left:145px;top:30px;color:var(--sky);font-weight:300;font-size:40px;letter-spacing:2px;line-height:1}
.brand small{display:block;font-size:15px;letter-spacing:5px;margin-top:8px;color:var(--sky)}
.search{position:absolute;left:763px;top:13px;width:236px;height:39px;display:flex}
.search span{flex:1;background:var(--white);font-size:12px;color:#555;padding:13px 0 0 20px}
.search b{width:39px;background:var(--sky);display:flex;align-items:center;justify-content:center}
.cart-icon{position:absolute;left:1013px;top:16px}
.main-nav{position:absolute;top:75px;left:0;width:1200px}
.main-nav a{position:absolute;color:var(--white);text-decoration:none;font-size:15px;font-weight:500}
.nav-mark{position:absolute;left:488px;top:58px}

/* Hero */
.hero{position:absolute;left:0;top:111px;width:1200px;height:580px;background:linear-gradient(90deg,#c9b9ac 0%,#8d7d73 22%,#a7a2a1 45%,#aaa5a5 100%)}
.hero h1{position:absolute;left:592px;top:74px;font-size:43px;font-weight:700;color:var(--white);letter-spacing:.3px}
.hero p{position:absolute;left:595px;top:143px;width:460px;font-size:19px;font-weight:700;color:var(--white);line-height:30px;text-align:justify}
.btn{display:flex;align-items:center;justify-content:center;background:var(--sky);color:var(--navy);font-weight:700;border-radius:40px;text-decoration:none}
.hero .btn{position:absolute;left:595px;top:235px;width:164px;height:59px;font-size:16px}
.dots span{position:absolute;left:1118px;width:13px;height:13px;border-radius:50%;background:var(--white)}
.hero-wave{position:absolute;left:0;top:500px}

/* Section titles */
.section-title{position:absolute;left:0;width:1200px;text-align:center;font-size:42px;font-weight:700;color:var(--ink);letter-spacing:.3px}

/* Products */
.product{position:absolute;width:212px}
.product-photo{height:257px;border:2px solid var(--line);position:relative;background:var(--white);overflow:hidden}
.product-photo .shot{position:absolute;inset:0}
.badge{position:absolute;right:12px;top:14px;color:var(--white);font-size:12px;font-weight:700;padding:2px 5px}
.product h3{text-align:center;font-size:17px;font-weight:600;margin-top:27px;letter-spacing:.2px}
.swatches{display:flex;justify-content:center;gap:9px;margin-top:15px}
.swatches i{width:16px;height:16px;border-radius:50%;display:block}
.swatches i.on{box-shadow:0 0 0 2px var(--white),0 0 0 3.5px var(--ink)}
.product .btn{width:125px;height:46px;margin:22px auto 0;font-size:12px}

/* Colours */
.colours-copy{position:absolute;left:0;top:1809px;width:600px;height:320px;background:var(--pale)}
.colours-copy h2{position:absolute;left:145px;top:30px;font-size:44px;font-weight:700}
.colours-copy p{position:absolute;left:145px;top:96px;width:430px;font-size:12px;line-height:25.5px;color:#444}
.colours-copy .btn{position:absolute;left:145px;top:220px;width:163px;height:59px;font-size:16px}
.colours-photo{position:absolute;left:600px;top:1809px;width:600px;height:320px;background:linear-gradient(90deg,#5b6fb5,#b0286e 18%,#c4402a 32%,#c9a0c8 46%,#c23870 58%,#e8a040 72%,#9a60c8 86%,#e07aa8)}

/* Blog */
.footer-scene{position:absolute;left:0;top:2827px;width:1200px;height:536px;background:linear-gradient(180deg,#8fa0b3 0%,#6f7f80 30%,#4d5a55 55%,#2a3440 100%)}
.post{position:absolute;top:2338px;height:489px;background:var(--white);border:1px solid #e2e4e6;text-align:center}
.post h4{font-size:15px;font-weight:500;margin-top:52px}
.post time{display:flex;justify-content:center;align-items:center;gap:4px;color:var(--date);font-size:12px;margin-top:12px}
.post p{width:246px;margin:12px auto 0;font-size:11px;line-height:22px;color:var(--text);text-align:justify;text-align-last:center}
.post .btn{position:absolute;left:50%;margin-left:-63px;width:126px;height:46px;font-size:12px}
.post-feature h4{margin-top:31px}
.post-feature p{text-align:center}
.post-photo{position:absolute;left:0;top:244px;width:100%;height:245px;background:linear-gradient(90deg,#b4a698 0%,#8a7a6a 30%,#c86a92 52%,#e07ab0 80%,#b84a7a 100%)}

/* Footer */
.footer-wave{position:absolute;left:0;top:2900px}
.footer-nav a{position:absolute;top:3179px;color:var(--white);font-size:16px;text-decoration:none}
.copyright{position:absolute;left:142px;top:3227px;color:var(--white);font-size:11.5px}
.payments{position:absolute;left:142px;top:3284px;display:flex;gap:9px}
.payments span{width:32px;height:22px;background:var(--white);border-radius:2px;font-size:7px;font-weight:700;color:var(--navy);display:flex;align-items:center;justify-content:center}
.footer-brand{position:absolute;left:739px;top:3170px;color:var(--sky);font-weight:300;font-size:42px;letter-spacing:2px;line-height:1;text-align:right;width:316px}
.footer-brand small{display:block;font-size:18px;letter-spacing:5px;margin-top:10px}
</style>
</head>
<body>

<header class="site-header">
  <div class="brand">VELMORA<small>HAIR BUILDING FIBRE</small></div>
  <div class="search"><span>Search</span><b><svg width="14" height="14" viewBox="0 0 14 14"><circle cx="6" cy="6" r="4" fill="none" stroke="#fff" stroke-width="2"/><path d="M9 9l4 4" stroke="#fff" stroke-width="2"/></svg></b></div>
  <svg class="cart-icon" width="40" height="34" viewBox="0 0 40 34" fill="none" stroke="#fff" stroke-width="1.6"><path d="M1 6h6l5 17h19l4-12H10"/><circle cx="14" cy="29" r="2.5"/><circle cx="28" cy="29" r="2.5"/><circle cx="32" cy="8" r="6"/><path d="M32 5v6M29 8h6"/></svg>
  <svg class="nav-mark" width="26" height="38" viewBox="0 0 26 38"><path d="M2 36L22 2" stroke="var(--sky)" stroke-width="1.5"/></svg>
  <nav class="main-nav">
    <a style="left:508px">HOME</a><a style="left:594px">ABOUT</a><a style="left:690px">PRODUCTS</a><a style="left:814px">NEWS</a><a style="left:898px">BLOG</a><a style="left:981px">CONTACT</a>
  </nav>
</header>

<section class="hero" role="img" aria-label="Photo of a woman with long, thick, glossy dark hair">
  <h1>HAIR BUILDING FIBRE</h1>
  <p>Lorem ipsum doloametconsectetur adipiscing elit, sed do eiusmod tempor incididunt</p>
  <a class="btn">SHOP NOW</a>
  <div class="dots"><span style="top:321px"></span><span style="top:345px;background:var(--sky)"></span><span style="top:369px"></span></div>
</section>
<svg class="hero-wave" width="1200" height="200" viewBox="0 0 1200 200">
  <path d="M0 92 C120 150 250 190 380 176 C560 150 640 30 860 26 C1000 24 1120 60 1200 96 L1200 200 L0 200Z" fill="var(--sky)"/>
  <path d="M0 106 C120 168 250 196 380 186 C560 170 640 52 860 44 C1000 40 1120 76 1200 110 L1200 200 L0 200Z" fill="#fff"/>
</svg>

<h2 class="section-title" style="top:744px">FEATURED PRODUCTS</h2>

<!-- Row 1 -->
<div class="product" style="left:142px;top:845px">
  <div class="product-photo"><div class="shot" role="img" aria-label="Product photo of the fibre canister in golden blonde" style="background:radial-gradient(ellipse 40% 48% at 50% 52%,#d9c49a 0%,#e6e1d8 55%,#fff 100%)"></div><span class="badge" style="background:var(--new)">NEW</span></div>
  <h3>PRODUCT NAME</h3>
  <div class="swatches"><i class="on" style="background:#d8a84a"></i><i style="background:#9c4a1a"></i><i style="background:#f1e4c8"></i><i style="background:#8a2a10"></i><i style="background:#3a0f12"></i><i style="background:linear-gradient(90deg,#e8a040,#f0c0a0)"></i><i style="background:linear-gradient(90deg,#d06a7a,#5ab0a0)"></i><i style="background:#6a1a6a"></i></div>
  <a class="btn">ADD TO CART</a>
</div>
<div class="product" style="left:377px;top:845px">
  <div class="product-photo"><div class="shot" role="img" aria-label="Product photo of the fibre canister in copper" style="background:radial-gradient(ellipse 40% 48% at 50% 52%,#c49078 0%,#e3dcd8 55%,#fff 100%)"></div></div>
  <h3>PRODUCT NAME</h3>
  <div class="swatches"><i style="background:#d8a84a"></i><i class="on" style="background:#9c4a1a"></i><i style="background:#f1e4c8"></i><i style="background:#8a2a10"></i><i style="background:#3a0f12"></i><i style="background:linear-gradient(90deg,#e8a040,#f0c0a0)"></i><i style="background:linear-gradient(90deg,#d06a7a,#5ab0a0)"></i><i style="background:#6a1a6a"></i></div>
  <a class="btn">ADD TO CART</a>
</div>
<div class="product" style="left:611px;top:845px">
  <div class="product-photo"><div class="shot" role="img" aria-label="Product photo of the fibre canister in platinum cream" style="background:radial-gradient(ellipse 40% 48% at 50% 52%,#e4ddcc 0%,#ecebe8 55%,#fff 100%)"></div><span class="badge" style="background:var(--sale)">SALE</span></div>
  <h3>PRODUCT NAME</h3>
  <div class="swatches"><i style="background:#d8a84a"></i><i style="background:#9c4a1a"></i><i class="on" style="background:#f1e4c8"></i><i style="background:#8a2a10"></i><i style="background:#3a0f12"></i><i style="background:linear-gradient(90deg,#e8a040,#f0c0a0)"></i><i style="background:linear-gradient(90deg,#d06a7a,#5ab0a0)"></i><i style="background:#6a1a6a"></i></div>
  <a class="btn">ADD TO CART</a>
</div>
<div class="product" style="left:845px;top:845px">
  <div class="product-photo"><div class="shot" role="img" aria-label="Product photo of the fibre canister in auburn" style="background:radial-gradient(ellipse 40% 48% at 50% 52%,#b98270 0%,#e2dad7 55%,#fff 100%)"></div></div>
  <h3>PRODUCT NAME</h3>
  <div class="swatches"><i style="background:#d8a84a"></i><i style="background:#9c4a1a"></i><i style="background:#f1e4c8"></i><i class="on" style="background:#8a2a10"></i><i style="background:#3a0f12"></i><i style="background:linear-gradient(90deg,#e8a040,#f0c0a0)"></i><i style="background:linear-gradient(90deg,#d06a7a,#5ab0a0)"></i><i style="background:#6a1a6a"></i></div>
  <a class="btn">ADD TO CART</a>
</div>

<!-- Row 2 -->
<div class="product" style="left:142px;top:1307px">
  <div class="product-photo"><div class="shot" role="img" aria-label="Product photo of the fibre canister in dark brown" style="background:radial-gradient(ellipse 40% 48% at 50% 52%,#8a7270 0%,#dedad9 55%,#fff 100%)"></div></div>
  <h3>PRODUCT NAME</h3>
  <div class="swatches"><i style="background:#d8a84a"></i><i style="background:#9c4a1a"></i><i style="background:#f1e4c8"></i><i style="background:#8a2a10"></i><i class="on" style="background:#3a0f12"></i><i style="background:linear-gradient(90deg,#e8a040,#f0c0a0)"></i><i style="background:linear-gradient(90deg,#d06a7a,#5ab0a0)"></i><i style="background:#6a1a6a"></i></div>
  <a class="btn">ADD TO CART</a>
</div>
<div class="product" style="left:377px;top:1307px">
  <div class="product-photo"><div class="shot" role="img" aria-label="Product photo of the fibre canister in peach pink" style="background:radial-gradient(ellipse 40% 48% at 50% 52%,#e2aa9e 0%,#ebe2df 55%,#fff 100%)"></div><span class="badge" style="background:var(--sale-2)">SALE</span></div>
  <h3>PRODUCT NAME</h3>
  <div class="swatches"><i style="background:#d8a84a"></i><i style="background:#9c4a1a"></i><i style="background:#f1e4c8"></i><i style="background:#8a2a10"></i><i style="background:#3a0f12"></i><i class="on" style="background:linear-gradient(90deg,#e8a040,#f0c0a0)"></i><i style="background:linear-gradient(90deg,#d06a7a,#5ab0a0)"></i><i style="background:#6a1a6a"></i></div>
  <a class="btn">ADD TO CART</a>
</div>
<div class="product" style="left:611px;top:1307px">
  <div class="product-photo"><div class="shot" role="img" aria-label="Product photo of the fibre canister in violet" style="background:radial-gradient(ellipse 40% 48% at 50% 52%,#b07ab0 0%,#e4dce4 55%,#fff 100%)"></div><span class="badge" style="background:var(--new)">NEW</span></div>
  <h3>PRODUCT NAME</h3>
  <div class="swatches"><i style="background:#d8a84a"></i><i style="background:#9c4a1a"></i><i style="background:#f1e4c8"></i><i style="background:#8a2a10"></i><i style="background:#3a0f12"></i><i style="background:linear-gradient(90deg,#e8a040,#f0c0a0)"></i><i style="background:linear-gradient(90deg,#d06a7a,#5ab0a0)"></i><i class="on" style="background:#6a1a6a"></i></div>
  <a class="btn">ADD TO CART</a>
</div>
<div class="product" style="left:845px;top:1307px">
  <div class="product-photo"><div class="shot" role="img" aria-label="Product photo of the fibre canister in rainbow pastel" style="background:radial-gradient(ellipse 40% 48% at 50% 52%,#c6aebc 0%,#e0e6e3 55%,#fff 100%)"></div></div>
  <h3>PRODUCT NAME</h3>
  <div class="swatches"><i style="background:#d8a84a"></i><i style="background:#9c4a1a"></i><i style="background:#f1e4c8"></i><i style="background:#8a2a10"></i><i style="background:#3a0f12"></i><i style="background:linear-gradient(90deg,#e8a040,#f0c0a0)"></i><i class="on" style="background:linear-gradient(90deg,#d06a7a,#5ab0a0)"></i><i style="background:#6a1a6a"></i></div>
  <a class="btn">ADD TO CART</a>
</div>

<section class="colours-copy">
  <h2>8 COLOURS</h2>
  <p>Lorem ipsum dolor sit amet, consectetur adipiscinged do eiusmod tempor incididunt ut labore et dolore magna aliqua.uis Iuspendisse ultrices gravisus commodo viverra maecenas accumsan lacus vel facili viverra maecenas accumsan lacsis.</p>
  <a class="btn">SHOP NOW</a>
</section>
<div class="colours-photo" role="img" aria-label="Strip of portraits of women with vividly coloured hair in blue, red, copper, lilac, pink and blonde"></div>

<h2 class="section-title" style="top:2230px">FROM THE BLOG</h2>

<div class="footer-scene" role="img" aria-label="Aerial view of a city skyline"></div>

<article class="post" style="left:144px;width:303px">
  <h4>AT VERO EOS EACCUSAMU</h4>
  <time><svg width="11" height="11" viewBox="0 0 11 11" fill="none" stroke="currentColor"><rect x="1" y="2" width="9" height="8"/><path d="M1 4.5h9M3 1v2M8 1v2"/></svg>Jan 25,2022</time>
  <p>At vero eos et accusamus et iusto odio dignissiducimomos ducimus qui blanditiis pducimuducimuraesentiuAt vero eos et accusamus et iusto odio dignissiducimumos ducimus landitiis pducimuducimurasentiu oluptatum deleniti atque corrupti quos dolores et quas molestias excepturi sint occaecati cupiditate non provident, similique sunt in culpa qui officia deserunt mollitia animi, id est laborum et dolorum fuga. Et harum quidem rerum facilis est et expedita distinctutvolupudiandae.</p>
  <a class="btn" style="top:416px">READ MORE</a>
</article>
<article class="post post-feature" style="left:447px;width:305px">
  <h4>AT VERO EOS EACCUSAMU</h4>
  <time><svg width="11" height="11" viewBox="0 0 11 11" fill="none" stroke="currentColor"><rect x="1" y="2" width="9" height="8"/><path d="M1 4.5h9M3 1v2M8 1v2"/></svg>Jan 25,2022</time>
  <p>At vero eos et accusamus et iusto odio dignissiducimumos ducimus qui blanditiis pducimuducimuraesentiu</p>
  <a class="btn" style="top:173px">READ MORE</a>
  <div class="post-photo" role="img" aria-label="Close-up of long ash blonde hair beside long pink hair"></div>
</article>
<article class="post" style="left:752px;width:303px">
  <h4>AT VERO EOS EACCUSAMU</h4>
  <time><svg width="11" height="11" viewBox="0 0 11 11" fill="none" stroke="currentColor"><rect x="1" y="2" width="9" height="8"/><path d="M1 4.5h9M3 1v2M8 1v2"/></svg>Jan 25,2022</time>
  <p>At vero eos et accusamus et iusto odio dignissiducimumos ducimus qui blanditiis pducimuducimuraesentiuAt vero eos et accusamus et iusto odio dignissiducimumos ducimus landitiis pducimuducimurasentiu oluptatum deleniti atque corrupti quos dolores et quas molestias excepturi sint occaecati cupiditate non provident, similique sunt in culpa qui officia deserunt mollitia animi, id est laborum et dolorum fuga. Et harum quidem rerum facilis est et expedita distinctutvolupudiandae.</p>
  <a class="btn" style="top:416px">READ MORE</a>
</article>

<svg class="footer-wave" width="1200" height="463" viewBox="0 0 1200 463">
  <path d="M0 110 C90 150 170 190 290 185 C480 170 620 30 860 22 C1000 18 1120 30 1200 40 L1200 463 L0 463Z" fill="var(--sky)"/>
  <path d="M0 120 C90 162 170 200 290 198 C480 190 620 48 860 38 C1000 34 1120 44 1200 54 L1200 463 L0 463Z" fill="var(--navy)"/>
</svg>

<nav class="footer-nav">
  <a style="left:142px">HOME</a><a style="left:230px">ABOUT</a><a style="left:324px">PRODUCTS</a><a style="left:448px">NEWS</a><a style="left:534px">BLOG</a><a style="left:616px">CONTACT</a>
</nav>
<p class="copyright">© 2022 Velmora Hairs. All rights reserved.Privacy | &nbsp;Terms of Use</p>
<div class="payments"><span>Vexa</span><span>Ordo</span><span>Nuvo</span><span>Amplo</span><span>Tilo</span></div>
<div class="footer-brand">VELMORA<small>HAIR BUILDING FIBRE</small></div>

</body>
</html>
```